Business Cards for 41Vale

I need business cards that goes with the logo
Updates

Dear designers - many thanks for the responsesreceived to date. There are many good designs but most of them are landscape.Could you please submit a few options for portrait layout as well.

Industry/Entity Type

Business

```html
<!DOCTYPE html>
<html lang="en">
<head>
<meta charset="utf-8">
<title>41Vale Business Card</title>
<link rel="stylesheet" href="https://fonts.googleapis.com/css2?family=Michroma&family=Questrial&display=swap">
<style>
  :root {
    --brand-red: #8c0000;
    --brand-red-light: #a50a0a;
    --brand-red-dark: #6e0000;
    --paper: #f6f6f6;
    --paper-shade: #e4e4e4;
    --ink: #1f1f1f;
    --white: #ffffff;
    --ghost: rgba(255,255,255,0.55);
  }
  * { margin: 0; padding: 0; box-sizing: border-box; }
  html, body { width: 1200px; height: 721px; overflow: hidden; background: var(--white); }
  .card {
    position: relative;
    width: 1200px;
    height: 721px;
    overflow: hidden;
    background: radial-gradient(ellipse at 75% 75%, var(--white) 0%, var(--paper) 45%, var(--paper-shade) 100%);
    font-family: "Questrial", "Century Gothic", sans-serif;
  }
  .ghost-wordmark {
    position: absolute;
    left: -60px;
    top: 20px;
    font-family: "Questrial", sans-serif;
    font-size: 520px;
    line-height: 1;
    color: var(--ghost);
    transform: rotate(12deg);
    transform-origin: left top;
    white-space: nowrap;
    letter-spacing: -10px;
  }
  .brand {
    position: absolute;
    right: 76px;
    top: 96px;
    display: flex;
    align-items: center;
    gap: 10px;
    color: var(--brand-red);
    font-size: 38px;
    letter-spacing: 0.5px;
  }
  .brand-dot {
    width: 18px; height: 18px; border-radius: 50%;
    background: var(--brand-red);
  }
  .name-band-highlight {
    position: absolute;
    left: 0; top: 338px;
    width: 592px; height: 30px;
    background: var(--white);
    border-radius: 0 8px 0 0;
  }
  .name-band-shadow {
    position: absolute;
    left: 0; top: 560px;
    width: 700px; height: 130px;
    background: radial-gradient(ellipse at 30% 0%, rgba(0,0,0,0.38) 0%, rgba(0,0,0,0.12) 45%, rgba(0,0,0,0) 72%);
  }
  .name-band {
    position: absolute;
    left: 0; top: 352px;
    width: 623px; height: 234px;
    border-radius: 0 8px 8px 0;
    background:
      linear-gradient(115deg, transparent 0 38%, rgba(255,255,255,0.05) 38% 62%, transparent 62%),
      linear-gradient(100deg, var(--brand-red-light) 0%, var(--brand-red) 55%, var(--brand-red-dark) 100%);
    box-shadow: 0 6px 14px rgba(0,0,0,0.25);
  }
  .person-name {
    position: absolute;
    right: 28px; top: 64px;
    font-family: "Michroma", "Eurostile", sans-serif;
    font-size: 44px;
    letter-spacing: 1px;
    color: var(--white);
    text-shadow: 0 2px 4px rgba(0,0,0,0.45);
    white-space: nowrap;
  }
  .person-title {
    position: absolute;
    right: 28px; top: 130px;
    font-size: 23px;
    letter-spacing: 1px;
    color: var(--white);
    white-space: nowrap;
  }
  .contact-list {
    position: absolute;
    right: 98px;
    top: 372px;
    list-style: none;
  }
  .contact-item {
    display: flex;
    justify-content: flex-end;
    align-items: center;
    height: 40.5px;
    font-size: 25px;
    letter-spacing: 1px;
    color: var(--ink);
  }
  .contact-icon {
    width: 34px; height: 30px;
    margin-left: 22px;
    margin-right: -56px;
    flex: none;
    fill: var(--brand-red);
  }
</style>
</head>
<body>
<main class="card">
  <div class="ghost-wordmark" aria-hidden="true">41Vale</div>

  <div class="brand"><span class="brand-name">41Vale</span><span class="brand-dot"></span></div>

  <div class="name-band-highlight"></div>
  <div class="name-band-shadow"></div>
  <section class="name-band">
    <h1 class="person-name">JOHN DOE</h1>
    <p class="person-title">EXECUTIVE VICE PRESIDENT</p>
  </section>

  <ul class="contact-list">
    <li class="contact-item"><span>123.4567.890</span>
      <svg class="contact-icon" viewBox="0 0 34 30" aria-label="Fax"><rect x="8" y="2" width="18" height="8"/><rect x="3" y="11" width="28" height="17" rx="2"/><rect x="8" y="15" width="18" height="3" fill="#f6f6f6"/></svg></li>
    <li class="contact-item"><span>123.4567.890</span>
      <svg class="contact-icon" viewBox="0 0 34 30" aria-label="Phone"><path d="M3 11 C3 3 31 3 31 11 L31 13 L24 13 L24 9 L10 9 L10 13 L3 13 Z"/><path d="M9 14 L25 14 L30 27 L4 27 Z"/><circle cx="17" cy="20" r="3.5" fill="#f6f6f6"/></svg></li>
    <li class="contact-item"><span>123.4567.890</span>
      <svg class="contact-icon" viewBox="0 0 34 30" aria-label="Mobile"><rect x="7" y="1" width="20" height="28" rx="3"/><rect x="10" y="4" width="14" height="7" fill="#f6f6f6"/><g fill="#f6f6f6"><rect x="10" y="14" width="3" height="3"/><rect x="15.5" y="14" width="3" height="3"/><rect x="21" y="14" width="3" height="3"/><rect x="10" y="19" width="3" height="3"/><rect x="15.5" y="19" width="3" height="3"/><rect x="21" y="19" width="3" height="3"/></g></svg></li>
    <li class="contact-item"><span>LoremIpsum.com</span>
      <svg class="contact-icon" viewBox="0 0 34 30" aria-label="Website"><text x="17" y="25" text-anchor="middle" font-family="Questrial, sans-serif" font-size="32" font-weight="700">@</text></svg></li>
    <li class="contact-item"><span>JohnDoe@LoremIpsum.com</span>
      <svg class="contact-icon" viewBox="0 0 34 30" aria-label="Email"><path d="M3 10 L17 2 L31 10 Z"/><path d="M3 12 L17 20 L31 12 L31 27 L3 27 Z"/></svg></li>
  </ul>
</main>
</body>
</html>
```